French version of popular website and translation

Translate existing website
Design simple copy of existing website in french

Logo stays the same
Content and pages stay the same

We just need to translate the website(s) and provide functional version of french website.

Please goto www.plivok.ca and new.plivok.ca

These 2 websites need to be copied, and 1 new french website needs to be created with existing content

We will then create a new website

www.plivok.ca/fr

There our new French website will be accessible, and our french team will be able to update it

Coding

Number of Pages Required

5+ page

Font styles to use
Sans Serif

Colors
cee9f5
cadf82
86cfc6
9bcb3b
aeded8
33b8a4
0dac94
00a990

Requirements
Must have
• Existing logo
• Existing photos from charities
• Existing information about our organization
Nice to have
• www.plivok.ca ( copy all pages with text and content)
• new.plivok.ca ( copy all pages with text and content)

```html
<!DOCTYPE html>
<html lang="fr">
<head>
<meta charset="UTF-8">
<title>plivok — Tout est vert.</title>
<link href="https://fonts.googleapis.com/css2?family=Roboto:wght@300;400;500&family=Roboto+Slab:wght@700&display=swap" rel="stylesheet">
<style>
  :root {
    --hero-deep: #26385a;
    --hero-mid: #4a5f86;
    --hero-light: #9aaccb;
    --text-light: #ffffff;
    --accent-green: #4f9a1c;
    --numeral: rgba(200,212,232,0.28);
  }
  * { margin: 0; padding: 0; box-sizing: border-box; }
  html, body { width: 1200px; height: 675px; overflow: hidden; }
  body { font-family: 'Roboto', Arial, sans-serif; color: var(--text-light); }
  .hero { position: relative; width: 1200px; height: 675px; overflow: hidden; }
  .hero-photo {
    position: absolute; inset: 0;
    background:
      radial-gradient(ellipse 420px 320px at 900px 300px, rgba(180,195,222,0.55), transparent 70%),
      linear-gradient(160deg, var(--hero-mid) 0%, var(--hero-light) 55%, var(--hero-mid) 75%, var(--hero-deep) 100%);
  }
  .hero-photo::after {
    content: ""; position: absolute; inset: 0;
    background: linear-gradient(90deg, rgba(38,56,90,0.75) 0%, rgba(38,56,90,0.25) 60%, rgba(38,56,90,0.45) 100%);
  }
  .brand {
    position: absolute; left: 28px; top: 32px;
    display: flex; align-items: center; gap: 9px;
    font-weight: 300; font-size: 18px; line-height: 1; letter-spacing: 0.4px;
  }
  .brand-mark { width: 10px; height: 10px; background: var(--text-light); display: block; }
  .main-nav { position: absolute; top: 34px; left: 418px; }
  .main-nav a {
    color: var(--text-light); text-decoration: none; font-weight: 300; font-size: 15.5px; letter-spacing: 0.2px;
    position: absolute; white-space: nowrap;
  }
  .social { position: absolute; top: 37px; left: 1013px; display: flex; gap: 18px; }
  .social span { width: 16px; height: 16px; border-radius: 50%; background: var(--text-light); display: block; }
  .headline {
    position: absolute; left: 30px; top: 136px; white-space: nowrap;
    font-family: 'Roboto Slab', Rockwell, Georgia, serif; font-weight: 700; font-size: 82px; letter-spacing: 1px; line-height: 1;
  }
  .slider-nav { position: absolute; top: 214px; left: 885px; width: 222px; height: 30px; }
  .slider-nav svg { position: absolute; top: 0; left: 0; }
  .slider-nav .label { position: absolute; top: 10px; font-size: 14px; font-weight: 300; }
  .intro {
    position: absolute; left: 46px; top: 310px; width: 440px;
    font-size: 14px; font-weight: 300; line-height: 26.4px;
  }
  .cta {
    position: absolute; left: 46px; top: 433px; width: 159px; height: 37px;
    background: var(--accent-green); color: var(--text-light);
    font-weight: 500; font-size: 14px; letter-spacing: 0.3px;
    display: flex; align-items: center; padding-left: 16px; gap: 8px; text-decoration: none;
  }
  .slide-dots { position: absolute; left: 1103px; top: 316px; display: flex; flex-direction: column; gap: 8px; }
  .slide-dots span { width: 9px; height: 9px; border: 1.5px solid var(--text-light); display: block; }
  .slide-dots .active { background: var(--accent-green); border-color: var(--accent-green); }
  .slide-number {
    position: absolute; left: 822px; top: 400px;
    font-family: 'Roboto Slab', Rockwell, Georgia, serif; font-weight: 700; font-size: 340px; line-height: 1;
    color: var(--numeral); letter-spacing: -6px;
  }
</style>
</head>
<body>
<section class="hero">
  <div class="hero-photo" role="img" aria-label="Photo de hautes herbes et roseaux sous un ciel brumeux, teintée de bleu"></div>

  <div class="slide-number">01</div>

  <div class="brand"><span class="brand-mark"></span>plivok</div>

  <nav class="main-nav">
    <a href="#" style="left:0">SUR</a>
    <a href="#" style="left:78px">MÉDIAS</a>
    <a href="#" style="left:184px">EMPLACEMENTS</a>
    <a href="#" style="left:363px">METTRE AU VERT</a>
  </nav>

  <div class="social" aria-label="Réseaux sociaux">
    <span></span><span></span><span></span><span></span><span></span>
  </div>

  <h1 class="headline">Tout est vert.</h1>

  <div class="slider-nav">
    <svg width="222" height="10" viewBox="0 0 222 10">
      <line x1="2" y1="5" x2="99" y2="5" stroke="#fff" stroke-width="1"/>
      <path d="M6 2 L1 5 L6 8" fill="none" stroke="#fff" stroke-width="1"/>
      <line x1="123" y1="5" x2="220" y2="5" stroke="#fff" stroke-width="1"/>
      <path d="M216 2 L221 5 L216 8" fill="none" stroke="#fff" stroke-width="1"/>
    </svg>
    <span class="label" style="left:67px">prev</span>
    <span class="label" style="left:124px">next</span>
  </div>

  <p class="intro">Faites partie de la révolution. Laissez-nous vous aider à atteindre<br>vos objectifs de responsabilité sociale pendant que nous rénovons<br>vos électrons non désirés et les donnons aux communautés dans<br>le besoin.</p>

  <a class="cta" href="#">LIRE LA SUITE
    <svg width="9" height="13" viewBox="0 0 9 13"><path d="M2 1.5 L7 6.5 L2 11.5" fill="none" stroke="#fff" stroke-width="2.4"/></svg>
  </a>

  <div class="slide-dots">
    <span class="active"></span><span></span><span></span>
  </div>
</section>
</body>
</html>
```